Professional Business Cards for Recruiting Company

We'd like professional 2-sided business cards that reflect a color scheme that matches our website, www.queryvantline.com, and / or logo that is attached.

Slogan used is "We Find Talent", but needs to be editable because we change it up to "We Know Developers", "We Speak Geek", etc.

Must includes logo, slogan, first and last name, address, email, mobile number and website address.

Files attached for ideas.

Thanks!

Contact Information for Business Card

Logo, Company name, First name, Last name, addresss, email, phone, website address.

Font styles to use
Sans Serif

Colors
0054AA
0677BA
7BADD7
CADEEF
E8F1F8

Requirements
Nice to have
• I do like the following designs. 22962062 and 22962651. Couple ideas anyway.

```html
<!DOCTYPE html>
<html lang="en">
<head>
<meta charset="utf-8">
<title>Queryvantline Business Card</title>
<link href="https://fonts.googleapis.com/css2?family=Montserrat:wght@300;400;600;700;800&display=swap" rel="stylesheet">
<style>
  :root {
    --navy: #17477f;
    --ink: #1f3f86;
    --text-dark: #1c2130;
    --text-grey: #4a4f5c;
    --rule: #3b5aa0;
    --paper: #ffffff;
    --backdrop: #ececec;
    --heading: #1f4c8c;
  }
  * { margin: 0; padding: 0; box-sizing: border-box; }
  html, body { width: 1200px; height: 1134px; overflow: hidden; }
  body {
    background: var(--backdrop);
    font-family: "Montserrat", sans-serif;
    position: relative;
  }
  .sheet-heading {
    position: absolute; top: 40px; left: 0; width: 1200px;
    text-align: center; color: var(--heading);
    font-weight: 600; font-size: 28px; line-height: 40px; letter-spacing: 0.5px;
  }
  .card {
    position: absolute; width: 700px; height: 400px;
    box-shadow: 0 10px 30px rgba(0,0,0,0.12);
    overflow: hidden;
  }
  .card-back { top: 160px; left: 420px; background: var(--navy); color: #fff; }
  .card-front { top: 620px; left: 80px; background: var(--paper); }

  /* back */
  .back-rule { position: absolute; left: 0; top: 250px; width: 660px; height: 2px; background: rgba(255,255,255,0.9); }
  .back-brand {
    position: absolute; left: 70px; top: 196px;
    display: flex; align-items: center; gap: 12px;
    background: var(--navy); padding: 0 14px 0 0;
  }
  .brand-square { width: 26px; height: 26px; background: #fff; }
  .back-brand .brand-name { font-weight: 700; font-size: 24px; letter-spacing: 1px; }
  .slogan {
    position: absolute; right: 72px; top: 264px;
    font-weight: 300; font-size: 30px; letter-spacing: 4px; text-transform: lowercase;
    white-space: nowrap;
  }

  /* front */
  .front-brand {
    position: absolute; right: 44px; top: 44px;
    display: flex; align-items: center; gap: 12px; color: var(--ink);
  }
  .front-brand .brand-square { background: var(--ink); width: 24px; height: 24px; }
  .front-brand .brand-name { font-weight: 600; font-size: 24px; letter-spacing: 1px; }
  .holder-name { position: absolute; left: 44px; top: 40px; font-weight: 800; font-size: 40px; color: var(--text-dark); }
  .holder-title { position: absolute; left: 46px; top: 98px; font-weight: 700; font-size: 18px; color: var(--ink); }
  .front-rule { position: absolute; left: 44px; top: 134px; width: 612px; height: 2px; background: var(--rule); }
  .contact-list { position: absolute; left: 46px; top: 156px; list-style: none; }
  .contact-list li {
    display: flex; align-items: center; gap: 10px;
    font-size: 17px; line-height: 30px; color: var(--text-grey);
  }
  .contact-list svg { width: 15px; height: 15px; fill: var(--ink); flex: none; }
  .contact-list .ext { color: var(--ink); font-weight: 700; }
  .company-block { position: absolute; right: 44px; bottom: 40px; text-align: right; }
  .company-name { font-weight: 800; font-size: 26px; color: var(--ink); letter-spacing: 1px; }
  .company-address { font-size: 17px; color: var(--text-grey); margin-top: 4px; }
</style>
</head>
<body>
  <h1 class="sheet-heading">BUSINESS CARD - MOCK UP 1<br>3.5IN X 2.0 IN &nbsp;|&nbsp; PRINT READY &nbsp;|&nbsp; 100% EDITABLE</h1>

  <section class="card card-back">
    <div class="back-rule"></div>
    <div class="back-brand">
      <span class="brand-square"></span>
      <span class="brand-name">QUERYVANTLINE</span>
    </div>
    <p class="slogan">we find talent</p>
  </section>

  <section class="card card-front">
    <h2 class="holder-name">Daniel Hervey</h2>
    <p class="holder-title">President</p>
    <div class="front-rule"></div>
    <ul class="contact-list">
      <li><svg viewBox="0 0 16 16"><path d="M3.5 1l2.5 3-1.5 1.6a9 9 0 0 0 5.9 5.9L12 10l3 2.5-1.7 2.3C7.5 14.5 1.5 8.5 1.2 2.7z"/></svg>555-014-2860 <span class="ext">ext.101</span></li>
      <li><svg viewBox="0 0 16 16"><path d="M4 0h8a1 1 0 0 1 1 1v14a1 1 0 0 1-1 1H4a1 1 0 0 1-1-1V1a1 1 0 0 1 1-1zm0 2v11h8V2z"/></svg>555-0139-6789</li>
      <li><svg viewBox="0 0 16 16"><path d="M0 3h16v10H0zm1.5 1.5v.3L8 9l6.5-4.2v-.3z"/></svg>dan.hervey@queryvantline.com</li>
      <li><svg viewBox="0 0 16 16"><circle cx="8" cy="8" r="7.5"/></svg>www.queryvantline.com</li>
    </ul>
    <div class="front-brand">
      <span class="brand-square"></span>
      <span class="brand-name">QUERYVANTLINE</span>
    </div>
    <div class="company-block">
      <p class="company-name">QUERYVANTLINE</p>
      <p class="company-address">Millbrook, Ohio</p>
    </div>
  </section>
</body>
</html>
```